Business Card Design Project

I need a business card for a Management Consultancy. We work with organisational design and development and strategic change using facilitation, consulting and coaching.

Size of card is 90 x 55mm.

Logo is attached.

Wording is:

Carla Brennick
Director

tel 0417286194
email is: info@bluepathvista.com.au

Target Market(s)

Government departments and not for profit organisations mainly.

Industry/Entity Type

Business

Requirements
Must have
• White or colour background not black.

On one side of the card, either back or front please include the words:

Leading Strategic Change

Two sided business card

```html
<!DOCTYPE html>
<html lang="en">
<head>
<meta charset="utf-8">
<title>BluePath Vista – Business Cards</title>
<link rel="stylesheet" href="https://fonts.googleapis.com/css2?family=Open+Sans:wght@400;600;700&display=swap">
<style>
  :root {
    --stage: #1d1d1f;
    --card-white: #ffffff;
    --leaf-green: #6cae2c;
    --leaf-green-dark: #579322;
    --slate-blue: #6f8ea8;
    --ring-blue: #7d9bb5;
    --ring-pale: #c9d6e1;
    --ink-grey: #4a4d52;
    --sky-blue: #5cb8e0;
    --steel-blue: #5f7d98;
    --deep-blue: #4d6984;
  }
  * { box-sizing: border-box; margin: 0; padding: 0; }
  html, body {
    width: 1200px; height: 1024px; overflow: hidden;
    background: var(--stage);
    font-family: "Open Sans", sans-serif;
  }
  .card-set { position: relative; width: 1200px; height: 1024px; }
  .card {
    position: absolute; top: 218px;
    width: 360px; height: 589px;
    border-radius: 4px; overflow: hidden;
    box-shadow: 0 10px 30px rgba(0,0,0,.45);
  }

  /* ---------- Front ---------- */
  .card-front { left: 180px; background: var(--card-white); }
  .card-front .shapes { position: absolute; inset: 0; }
  .brand-mark {
    position: absolute; top: 58px; left: 0; right: 0;
    display: flex; justify-content: center; align-items: center; gap: 10px;
  }
  .brand-dot {
    width: 26px; height: 26px; border-radius: 50%;
    background: var(--slate-blue);
  }
  .brand-name {
    font-weight: 700; font-size: 27px; color: var(--slate-blue);
    letter-spacing: -0.3px;
  }
  .contact {
    position: absolute; top: 188px; left: 72px; width: 230px;
    color: var(--ink-grey); font-size: 15px; line-height: 21px;
    white-space: nowrap;
  }
  .contact .person-name {
    color: var(--leaf-green); font-weight: 700; font-size: 23px; line-height: 30px;
    text-align: center;
  }
  .contact .person-role {
    font-size: 17px; line-height: 22px; text-align: center; margin-bottom: 6px;
  }
  .contact .label { color: var(--leaf-green); }
  .web-front {
    position: absolute; bottom: 34px; left: 44px;
    color: var(--card-white); font-size: 17px; font-weight: 600;
  }

  /* ---------- Back ---------- */
  .card-back {
    left: 660px;
    background: linear-gradient(160deg, var(--sky-blue) 0%, var(--steel-blue) 45%, var(--deep-blue) 100%);
  }
  .ring-decoration {
    position: absolute; top: 0; left: 0; width: 360px; height: 400px;
    background: radial-gradient(circle at 62% 34%, rgba(200,230,245,.75) 0%, rgba(140,190,220,.45) 35%, rgba(95,125,152,0) 70%);
  }
  .back-brand {
    position: absolute; top: 414px; left: 0; right: 0;
    display: flex; justify-content: center; align-items: center; gap: 10px;
  }
  .back-brand .brand-dot { background: var(--card-white); }
  .back-brand .brand-name { color: var(--card-white); font-size: 30px; }
  .web-back {
    position: absolute; top: 470px; left: 0; right: 0; text-align: center;
    color: var(--card-white); font-size: 16px; font-weight: 600;
  }
  .tagline {
    position: absolute; top: 510px; left: 0; right: 0; text-align: center;
    color: var(--card-white); font-size: 15px; font-weight: 400;
    letter-spacing: 1.5px; text-transform: uppercase;
  }
</style>
</head>
<body>
<main class="card-set">

  <section class="card card-front" aria-label="Card front">
    <svg class="shapes" width="360" height="589" viewBox="0 0 360 589" aria-hidden="true">
      <path d="M0 360 Q180 470 360 330 L360 589 L0 589 Z" fill="var(--leaf-green)"/>
      <path d="M0 380 Q180 490 360 350 L360 362 Q180 500 0 392 Z" fill="var(--leaf-green-dark)" opacity=".5"/>
      <circle cx="185" cy="280" r="168" fill="var(--card-white)"/>
      <circle cx="185" cy="280" r="168" fill="none" stroke="var(--ring-blue)" stroke-width="13"/>
      <circle cx="185" cy="280" r="140" fill="none" stroke="var(--ring-pale)" stroke-width="8"/>
    </svg>

    <div class="brand-mark">
      <span class="brand-dot"></span>
      <span class="brand-name">BluePath Vista</span>
    </div>

    <div class="contact">
      <p class="person-name">Carla Brennick</p>
      <p class="person-role">Director</p>
      <p><span class="label">Phone :</span> 0417286194</p>
      <p><span class="label">Fax :</span> 02 8011 7402</p>
      <p>info@bluepathvista.com.au</p>
      <p>Your address goes here, Street,</p>
      <p>City, Zip Code</p>
    </div>

    <p class="web-front">www.bluepathvista.com.au</p>
  </section>

  <section class="card card-back" aria-label="Card back">
    <div class="ring-decoration" role="img" aria-label="Large soft ring decoration in light blue tones"></div>
    <div class="back-brand">
      <span class="brand-dot"></span>
      <span class="brand-name">BluePath Vista</span>
    </div>
    <p class="web-back">www.bluepathvista.com.au</p>
    <p class="tagline">Leading Strategic Change</p>
  </section>

</main>
</body>
</html>
```